K & D A/C Compressors' Business Card

Hello,

I need someone to create a new business card for my business. The name of my Business is: K & D A/C Compressors. I sell automotive air conditioning parts (a/c parts). I would like the business card to incorporate my logo, and to have an automotive feel to it. It is important that the business card feel like it is coming from an automotive parts business.

I already have a logo, which I will provide.

Thanks.
Updates

Project Deadline Extended Reason: I feel like extending the deadline until October 9, 2017, will allow for more time to design the business card. Thank you for your understanding. Added Monday, October 2, 2017

Target Market(s)

Consumers who need automotive a/c parts, and auto mechanics.

Industry/Entity Type

Automotive

Contact Information for Business Card

Business name: K & D A/C Compressors
Business Address: 48207 Southwest 36th Street, Bayview Park, Florida 33990
Telephone: 305-472-1390
Fax: To be provided once I choose your design.
Website: www.kdcoolunits.example
Email: support@kdcoolunits.example
Names: To be provided once I choose your design.

Font styles to use
Sans Serif

Colors

Designer to choose colors to be used in the design.

Requirements
Must have
• The business card must include all of the "Business Card Details" and the logo I have uploaded.

```html
<!DOCTYPE html>
<html lang="en">
<head>
<meta charset="utf-8">
<title>K &amp; D A/C Compressors – Business Card</title>
<link rel="stylesheet" href="https://fonts.googleapis.com/css2?family=Montserrat:wght@400;500;700;800&display=swap">
<style>
  :root {
    --navy: #2a2937;
    --teal: #0099bf;
    --paper: #f3f3f1;
    --ink: #2a2937;
    --grey: #8d8d8d;
    --muted: #b9b9c0;
    --stage: #c9c9c9;
  }
  * { box-sizing: border-box; margin: 0; padding: 0; }
  html, body { width: 1200px; height: 1152px; overflow: hidden; }
  body {
    background: var(--stage);
    font-family: "Montserrat", Arial, sans-serif;
    position: relative;
  }
  .card {
    position: absolute;
    left: 150px;
    width: 900px;
    height: 514px;
    overflow: hidden;
    box-shadow: 0 6px 20px rgba(0,0,0,.18);
  }

  /* Back side */
  .card-back { top: 40px; background: var(--navy); }
  .back-panel {
    position: absolute; inset: 40px;
    background: var(--paper);
    border-radius: 36px;
    display: flex; align-items: center; justify-content: center;
  }
  .back-name {
    font-size: 52px; font-weight: 500; color: var(--grey);
    letter-spacing: .5px; display: flex; align-items: center; gap: 22px;
  }
  .back-name .mark { width: 36px; height: 36px; background: var(--grey); flex: none; }

  /* Front side */
  .card-front { top: 598px; background: var(--paper); }
  .blue-panel {
    position: absolute; left: 60px; top: 24px; width: 700px; height: 340px;
    background: var(--teal);
    border-radius: 44px 80px 0 0;
  }
  .dark-band {
    position: absolute; left: 0; right: 0; top: 300px; height: 186px;
    background: var(--navy);
  }
  .front-name {
    position: absolute; left: 100px; top: 60px;
    font-size: 44px; font-weight: 500; color: var(--navy);
    letter-spacing: .5px; white-space: nowrap;
  }
  .contact {
    position: absolute; left: 100px; top: 146px;
    display: grid; grid-template-columns: 62px auto; column-gap: 20px; row-gap: 4px;
    font-size: 17px; color: var(--ink); line-height: 1.3;
  }
  .contact dt { font-weight: 800; text-align: right; }
  .contact dd { font-weight: 500; white-space: nowrap; }
  .product-photo {
    position: absolute; left: 560px; top: 140px; width: 290px; height: 230px;
    background: linear-gradient(135deg, #d8dadc 0%, #9fa3a7 55%, #4a4d52 100%);
    border-radius: 6px;
  }
  .person {
    position: absolute; left: 70px; top: 330px;
    display: flex; align-items: center; gap: 18px;
  }
  .person-name { font-size: 26px; font-weight: 800; color: var(--teal); line-height: 1.1; }
  .person-role { font-size: 24px; font-weight: 500; color: var(--muted); line-height: 1.1; }
  .address {
    position: absolute; left: 430px; top: 400px;
    display: flex; align-items: center; gap: 18px;
  }
  .address p { font-size: 19px; font-weight: 500; color: #fff; line-height: 1.35; white-space: nowrap; }
</style>
</head>
<body>

<section class="card card-back" aria-label="Card back">
  <div class="back-panel">
    <div class="back-name"><span class="mark"></span>K &amp; D A/C Compressors</div>
  </div>
</section>

<section class="card card-front" aria-label="Card front">
  <div class="blue-panel"></div>
  <div class="dark-band"></div>

  <div class="front-name">K &amp; D A/C Compressors</div>

  <dl class="contact">
    <dt>TEL</dt><dd>305-472-1390</dd>
    <dt>FAX</dt><dd>000-000-0000</dd>
    <dt>WEB</dt><dd>www.kdcoolunits.example</dd>
    <dt>EMAIL</dt><dd>support@kdcoolunits.example</dd>
  </dl>

  <div class="product-photo" role="img" aria-label="Photo of automotive A/C parts: condenser, radiator fan, compressor and drier"></div>

  <div class="person">
    <svg width="60" height="52" viewBox="0 0 60 52" aria-hidden="true">
      <circle cx="30" cy="16" r="14" fill="#0099bf"/>
      <path d="M4 52 C6 34 18 30 30 30 C42 30 54 34 56 52 Z" fill="#0099bf"/>
    </svg>
    <div>
      <div class="person-name">YOUR NAME</div>
      <div class="person-role">Founder</div>
    </div>
  </div>

  <div class="address">
    <svg width="34" height="48" viewBox="0 0 34 48" aria-hidden="true">
      <path d="M17 0 C7.6 0 0 7.6 0 17 C0 29 17 48 17 48 C17 48 34 29 34 17 C34 7.6 26.4 0 17 0 Z" fill="#0099bf"/>
      <circle cx="17" cy="17" r="7" fill="#2a2937"/>
    </svg>
    <p>48207 Southwest 36th Street,<br>Bayview Park, Florida 33990</p>
  </div>
</section>

</body>
</html>
```